Copper Meadow Creamery Business cards

We need a logo design for our family dairy. Included on the cards should be my name/my husbands name/the dairy name/ all the phone numbers/address and email. The name is Copper Meadow Creamery, LLC. We would like to use our farm mascot pic on the card. We know the pictures I sent you are of a beef cow but she is the mascot of the farm. We were thinking that maybe put a picture of her head in the middle of the card with a "B" on one side and a "D" on the other side with a "C" around the picture of the cow. But we are open to any ideas. We are looking for something kind of professional and a design that that can be used on cards, clothing and a car sign. Black lettering and blue for the other color...or what looks good.

Target Market(s)

All

Industry/Entity Type

Farming

Contact Information for Business Card

Marla Dutton Owner (555)417-2093
Ronald Pfister Owner (555)238-7715
Copper Meadow Creamery, LLC (555)906-4182
Coppermeadowcreamery@mailbarn.test
7126 County Lane 91, Alder Ridge, QX 50917

Font styles to use
Sans Serif

Colors
3176b5
3c7bb8
3277b5
0255a3

Requirements
Must have
• Some design that incorporates a drawing/pic of the cow pictures that were sent.
Nice to have
• no suggestions
Should not have
• no suggestions

```html
<!DOCTYPE html>
<html lang="en">
<head>
<meta charset="utf-8">
<title>Copper Meadow Creamery – Business Card</title>
<link href="https://fonts.googleapis.com/css2?family=Montserrat:wght@400;600;700&display=swap" rel="stylesheet">
<style>
  :root {
    --page-bg: #ececec;
    --card-bg: #f7f7f7;
    --brand-blue: #4068ae;
    --brand-blue-deep: #3a5fa6;
    --name-blue: #4470b6;
    --ink: #2a2a2a;
    --mascot-tone-a: #8a7a62;
    --mascot-tone-b: #4a4038;
  }
  * { box-sizing: border-box; margin: 0; padding: 0; }
  html, body {
    width: 1200px; height: 787px; overflow: hidden;
    background: var(--page-bg);
    font-family: "Montserrat", sans-serif;
  }
  .business-card {
    position: absolute; left: 150px; top: 136px;
    width: 900px; height: 514px;
    background: var(--card-bg);
    box-shadow: 0 10px 30px rgba(0,0,0,0.12);
    overflow: hidden;
  }
  .brand-band {
    position: absolute; left: 0; top: 0; width: 100%; height: 200px;
    background: linear-gradient(90deg, var(--brand-blue-deep), var(--brand-blue));
    display: flex; align-items: center; justify-content: center;
  }
  .brand-lockup {
    display: flex; align-items: center; gap: 22px;
  }
  .mascot-photo {
    flex: none;
    width: 80px; height: 80px; border-radius: 50%;
    background: radial-gradient(circle at 40% 40%, var(--mascot-tone-a), var(--mascot-tone-b));
    border: 3px solid #ffffff;
  }
  .brand-name {
    color: #ffffff; font-weight: 600; font-size: 38px; letter-spacing: 1px;
    white-space: nowrap;
  }
  .owner {
    position: absolute; font-size: 24px; color: var(--ink); line-height: 1.35;
    white-space: nowrap;
  }
  .owner-name { color: var(--name-blue); font-weight: 700; text-transform: uppercase; }
  .owner-title { font-weight: 400; }
  .owner--first { left: 42px; top: 222px; }
  .owner--second { left: 470px; top: 222px; }
  .company {
    position: absolute; left: 42px; top: 318px;
    font-size: 24px; line-height: 1.35; color: var(--ink);
    white-space: nowrap;
  }
  .company-name { font-weight: 700; }
  .bottom-rule {
    position: absolute; left: 0; bottom: 50px; width: 100%; height: 4px;
    background: var(--brand-blue);
  }
  .bottom-stripe {
    position: absolute; left: 0; bottom: 26px; width: 100%; height: 16px;
    background: var(--brand-blue);
  }
</style>
</head>
<body>
  <div class="business-card">
    <div class="brand-band">
      <div class="brand-lockup">
        <div class="mascot-photo" role="img" aria-label="Photo of the farm mascot cow's head"></div>
        <div class="brand-name">Copper Meadow Creamery</div>
      </div>
    </div>

    <div class="owner owner--first">
      <div><span class="owner-name">Marla Dutton,</span> <span class="owner-title">Owner</span></div>
      <div>(555)417-2093</div>
    </div>

    <div class="owner owner--second">
      <div><span class="owner-name">Ronald Pfister,</span> <span class="owner-title">Owner</span></div>
      <div>(555)238-7715</div>
    </div>

    <div class="company">
      <div><span class="company-name">Copper Meadow Creamery, LLC</span> (555)906-4182</div>
      <div>coppermeadowcreamery@mailbarn.test</div>
      <div>7126 County Lane 91, Alder Ridge, QX 50917</div>
    </div>

    <div class="bottom-rule"></div>
    <div class="bottom-stripe"></div>
  </div>
</body>
</html>
```